Business Card Design

I am an Event and Wedding Planner in need of an eye catching business card featuring my logo (attached), my contact details, and my company tagline (Making each one of your gatherings radiant...) I would like the tagline in font similar the logo's font.
Updates
I have just noticed that my logo has a misspelling so for the final design, I will be uploading a corrected logo as soon as I have it.
My apologies.
Reason: Waiting on a corrected logo...Occasions is misspelled and it should say Weddings not Wedding
The logo has been corrected so now Occasions is spelled correctly and it says Weddings instead of Wedding. Please use Edwardian Script ITC as the font for the tagline so it will match the logo. Thank you for your patience.
Target Market(s)
Engaged couples and people hosting milestone celebrations. 25-50 years old, predominately female
Industry/Entity Type
Business
Contact Information for Business Card
Delphine Marsh, Event Manager / Owner, Mobile: 0491 836 254, Email: delphine@radiantgatheringsco.com.au, www.radiantgatheringsco.com.au, Making each one of your gatherings radiant...

```html
<!DOCTYPE html>
<html lang="en">
<head>
<meta charset="utf-8">
<title>Radiant Gatherings Co — Business Card</title>
<link rel="stylesheet" href="https://fonts.googleapis.com/css2?family=Pinyon+Script&family=Arimo:wght@400&family=Tinos:ital@1&display=swap">
<style>
  :root {
    --page: #ffffff;
    --card: #6d6e70;
    --card-edge: #7c7d80;
    --ink-dark: #2e2e30;
    --ink-light: #ffffff;
    --accent-red: #c0281e;
    --petal: #b5402a;
  }
  * { box-sizing: border-box; margin: 0; padding: 0; }
  html, body { width: 1200px; height: 1000px; overflow: hidden; background: var(--page); }
  .canvas { position: relative; width: 1200px; height: 1000px; }

  .card {
    position: absolute;
    background: var(--card);
    border: 1px solid var(--card-edge);
    box-shadow: 0 4px 10px rgba(0,0,0,0.35);
  }

  /* Front */
  .card--front { left: 50px; top: 40px; width: 728px; height: 438px; }
  .brand-name {
    position: absolute; left: 0; right: 0; top: 150px;
    text-align: center;
    font-family: "Arimo", sans-serif; font-weight: 400;
    font-size: 40px; line-height: 1;
    color: var(--ink-dark);
  }
  .front-ornament {
    position: absolute; left: 329px; top: 240px;
    width: 70px; height: 64px;
  }
  .tagline-rule {
    position: absolute; left: 150px; width: 430px; top: 332px;
    height: 1px; background: var(--accent-red);
  }
  .tagline {
    position: absolute; left: 0; right: 0; top: 342px;
    text-align: center;
    font-family: "Pinyon Script", cursive;
    font-size: 30px; color: var(--accent-red);
  }

  /* Back */
  .card--back { left: 400px; top: 512px; width: 728px; height: 438px; }
  .holder { position: absolute; left: 12px; top: 28px; }
  .holder__name {
    font-family: "Arimo", sans-serif; font-size: 18px;
    color: var(--ink-light); letter-spacing: 0.3px;
  }
  .holder__role {
    font-family: "Tinos", serif; font-style: italic;
    font-size: 14px; color: var(--ink-dark); line-height: 1;
  }
  .contact-list { position: absolute; left: 12px; top: 140px; list-style: none; }
  .contact-list li {
    display: flex; align-items: center; gap: 10px;
    height: 31px;
    font-family: "Arimo", sans-serif; font-size: 18px; color: var(--ink-light);
  }
  .contact-list svg { width: 28px; height: 24px; flex: none; }
  .back-brand {
    position: absolute; right: 40px; top: 300px; width: 300px;
    text-align: center;
    font-family: "Arimo", sans-serif; font-weight: 400;
    font-size: 26px; line-height: 1.2; color: var(--ink-dark);
  }
</style>
</head>
<body>
<main class="canvas">

  <section class="card card--front">
    <p class="brand-name">Radiant Gatherings Co</p>
    <svg class="front-ornament" viewBox="0 0 70 64" role="img" aria-label="Small red four-petal flower ornament">
      <rect x="0" y="0" width="70" height="64" rx="14" fill="var(--petal)"/>
    </svg>
    <div class="tagline-rule"></div>
    <p class="tagline">Making each one of your gatherings radiant...</p>
  </section>

  <section class="card card--back">
    <div class="holder">
      <p class="holder__name">DELPHINE MARSH</p>
      <p class="holder__role">Event Manager / Owner</p>
    </div>

    <ul class="contact-list">
      <li>
        <svg viewBox="0 0 28 24" aria-hidden="true">
          <rect x="2" y="3" width="24" height="18" fill="none" stroke="#fff" stroke-width="2"/>
          <path d="M2 3 L14 14 L26 3" fill="none" stroke="#fff" stroke-width="2"/>
        </svg>
        delphine@radiantgatheringsco.com.au
      </li>
      <li>
        <svg viewBox="0 0 28 24" aria-hidden="true">
          <path d="M2 9 Q14 1 26 9 L23 12 L19 10 L19 7 Q14 5 9 7 L9 10 L5 12 Z" fill="#fff"/>
          <rect x="6" y="13" width="16" height="9" rx="1" fill="#fff"/>
          <circle cx="14" cy="17.5" r="2.5" fill="var(--card)"/>
        </svg>
        0491 836 254
      </li>
      <li>
        <svg viewBox="0 0 28 24" aria-hidden="true">
          <g fill="none" stroke="#fff" stroke-width="1.6">
            <circle cx="14" cy="12" r="10"/>
            <ellipse cx="14" cy="12" rx="4.5" ry="10"/>
            <line x1="4" y1="12" x2="24" y2="12"/>
            <line x1="6" y1="6.5" x2="22" y2="6.5"/>
            <line x1="6" y1="17.5" x2="22" y2="17.5"/>
          </g>
        </svg>
        www.radiantgatheringsco.com.au
      </li>
    </ul>

    <p class="back-brand">Radiant Gatherings Co</p>
  </section>

</main>
</body>
</html>
```